Maple Sprouts Childcare requires Double sided A6 Flyer

Design a double sided A6 flyer (105mm x 148mm) flyer for a childcare centre to promote more business. The copy for the flyer is attached so please use this copy is in the flyer so we can see what the final design would look like.

The childcare is wanting more children aged 0-5 years to come to their daycare so it needs to appeal to parents of young children and get them to come an see the centre.

The colours and fonts used should align with the style guide and logo. The client is ok to use Maple sprouts as icons if you wish but must look professional and link with the brand.

You can also look at their website for further insights - maplesproutschildcare.example.au

Target Market(s)

Parents of children aged 0-5 years located within a 10km radius of the child care centre.

Industry/Entity Type

Childcare

Font styles to use
Other font styles liked:
• Please use the style guide for fonts.

Requirements
Must have
• Be appealing and make the audience want to read the flyer and act on it.
Nice to have
• As it is a childcare it can be playful, colourful and personable. It must still look professional and modern.

```html
<!DOCTYPE html>
<html lang="en">
<head>
<meta charset="utf-8">
<title>Maple Sprouts Childcare – Flyer</title>
<link rel="stylesheet" href="https://fonts.googleapis.com/css2?family=Sniglet:wght@800&family=Patrick+Hand&display=swap">
<style>
  :root {
    --paper: #fbeea0;
    --paper-edge: #f6e27a;
    --purple: #3b2c78;
    --green: #2e8a3c;
    --body-green: #2b6b35;
    --photo-frame: #ffffff;
    --tape: rgba(214, 196, 150, 0.75);
    --photo-left-a: #8a6f55;
    --photo-left-b: #c9b79c;
    --photo-right-a: #d8d3c8;
    --photo-right-b: #8d8c95;
  }
  * { box-sizing: border-box; margin: 0; padding: 0; }
  html, body { width: 878px; height: 1200px; overflow: hidden; background: #ffffff; }
  .flyer {
    position: relative;
    width: 878px;
    height: 1200px;
    overflow: hidden;
    background: radial-gradient(ellipse at center, var(--paper) 55%, var(--paper-edge) 100%);
  }
  .headline {
    position: absolute;
    top: 70px; left: 40px; right: 40px;
    text-align: center;
    font-family: "Sniglet", "Comic Sans MS", cursive;
    font-weight: 800;
    font-size: 41px;
    line-height: 1.2;
    letter-spacing: 1px;
    text-transform: uppercase;
    color: var(--purple);
  }
  .intro {
    position: absolute;
    top: 205px; left: 80px; right: 80px;
    text-align: center;
    font-family: "Patrick Hand", "Comic Sans MS", cursive;
    font-size: 25px;
    line-height: 1.25;
    letter-spacing: 0.5px;
    text-transform: uppercase;
    color: var(--green);
    font-weight: bold;
  }
  .snapshot {
    position: absolute;
    background: var(--photo-frame);
    padding: 14px;
    box-shadow: 0 4px 10px rgba(0,0,0,0.25);
  }
  .snapshot-fill { width: 100%; height: 100%; }
  .snapshot--left { left: 122px; top: 322px; width: 278px; height: 350px; transform: rotate(-3deg); }
  .snapshot--left .snapshot-fill { background: linear-gradient(160deg, var(--photo-left-b), var(--photo-left-a)); }
  .snapshot--right { left: 412px; top: 360px; width: 312px; height: 360px; transform: rotate(3deg); }
  .snapshot--right .snapshot-fill { background: linear-gradient(200deg, var(--photo-right-a), var(--photo-right-b)); }
  .tape {
    position: absolute;
    top: -14px; left: 50%;
    width: 40px; height: 46px;
    margin-left: -20px;
    background: var(--tape);
  }
  .about {
    position: absolute;
    top: 755px; left: 108px; width: 600px;
    font-family: "Patrick Hand", "Comic Sans MS", cursive;
    font-size: 20px;
    line-height: 1.2;
    letter-spacing: 0.5px;
    text-transform: uppercase;
    color: var(--body-green);
  }
  .tagline {
    position: absolute;
    top: 962px; left: 112px; width: 470px;
    font-family: "Sniglet", "Comic Sans MS", cursive;
    font-weight: 800;
    font-size: 24px;
    line-height: 1.3;
    text-transform: uppercase;
    color: var(--purple);
  }
  .brand {
    position: absolute;
    left: 590px; top: 1100px;
    display: flex; align-items: center; gap: 12px;
    font-family: "Sniglet", "Comic Sans MS", cursive;
    font-weight: 800;
    font-size: 34px;
    text-transform: uppercase;
    color: var(--purple);
  }
  .brand-dot { width: 22px; height: 22px; border-radius: 50%; background: var(--green); }
</style>
</head>
<body>
  <main class="flyer">
    <h1 class="headline">Specialising in long day care<br>and out of school care</h1>
    <p class="intro">The environment in our centre is a stimulating one where children feel safe and supported in their explorations.</p>

    <figure class="snapshot snapshot--left">
      <span class="tape"></span>
      <div class="snapshot-fill" role="img" aria-label="Photo of a wooden tub filled with chunky coloured pencils"></div>
    </figure>
    <figure class="snapshot snapshot--right">
      <span class="tape"></span>
      <div class="snapshot-fill" role="img" aria-label="Photo of a bright play room with shelves of toys and a blue rug"></div>
    </figure>

    <p class="about">We recognise that each stage of development is a unique and valuable part of life and we provide opportunities for children to explore, question and gain experiences to maximize their growth and confidence. Our focus is to create an environment where children and families feel a sense of “being, belonging and becoming.</p>

    <p class="tagline">Where we recognise that small things matter the most . . .</p>

    <div class="brand"><span class="brand-dot"></span>Maple Sprouts</div>
  </main>
</body>
</html>
```